Morvaleth Company Notepad / Grid pad / Graph pad

I need a "modern" version of this graph pad. The information at the top needs to be shown, along with the graph lines, however, I need this more "interesting" than it currently is. This will be printed and bound at the TOP edge with 50 sheets per pack.

Target Market(s)

Clients - Want to show sophistication and not childish.

Industry/Entity Type

Structural Engineering

Font styles to use
Sans Serif

Colors
0255a3
85abd2

Requirements
Must have
• My project must have all of the elements currently shown on the pdf
Should not have
• My project should not have clipart images.

```html
<!DOCTYPE html>
<html lang="en">
<head>
<meta charset="utf-8">
<title>Morvaleth Company Graph Pad</title>
<link href="https://fonts.googleapis.com/css2?family=Montserrat:wght@400;500;700&display=swap" rel="stylesheet">
<style>
  :root {
    --brand-blue: #0255a3;
    --brand-sky: #85abd2;
    --ink: #2a2f36;
    --muted: #6b7480;
    --rule: #8a9099;
    --grid-line: #d9dce0;
    --frame: #1d1f22;
    --paper: #ffffff;
    --backdrop: #e8eaed;
  }
  * { box-sizing: border-box; margin: 0; padding: 0; }
  html, body {
    width: 1200px; height: 586px; overflow: hidden;
    background: var(--backdrop);
    font-family: "Montserrat", sans-serif;
  }
  .canvas { position: relative; width: 1200px; height: 586px; }
  .sheet {
    position: absolute; left: 383px; top: 13px;
    width: 433px; height: 560px;
    background: var(--paper);
    overflow: hidden;
    box-shadow: 0 2px 10px rgba(0,0,0,.12);
  }
  .header-wave { position: absolute; top: 0; left: 0; width: 433px; height: 62px; }
  .brand { position: absolute; left: 31px; top: 22px; width: 130px; text-align: center; }
  .brand-name {
    display: block;
    font-size: 14px; font-weight: 700; line-height: 1.1;
    letter-spacing: .2px; color: var(--brand-blue);
  }
  .brand-tagline {
    display: block; margin-top: 5px;
    font-size: 4.6px; font-weight: 500; color: var(--muted);
  }
  .contact {
    position: absolute; left: 196px; top: 17px;
    font-style: normal;
    font-size: 5.6px; font-weight: 500; line-height: 1.35; color: var(--ink);
  }
  .fields { position: absolute; left: 196px; top: 41px; width: 211px; }
  .field-row { display: flex; align-items: flex-end; height: 10.3px; font-size: 5.6px; color: var(--ink); }
  .field { display: flex; align-items: flex-end; }
  .field-label { white-space: nowrap; margin-right: 4px; }
  .field-line { flex: 1; border-bottom: 0.6px solid var(--rule); height: 5px; }
  .field--wide { width: 122px; }
  .field--narrow { flex: 1; }
  .field--page { width: 66px; }
  .field--of { width: 56px; }
  .field--of .field-label { margin: 0 4px; }
  .grid-area {
    position: absolute; left: 28px; top: 82px;
    width: 379px; height: 451px;
    border: 1px solid var(--frame);
    background-color: var(--paper);
    background-image:
      linear-gradient(to right, var(--grid-line) 0.6px, transparent 0.6px),
      linear-gradient(to bottom, var(--grid-line) 0.6px, transparent 0.6px);
    background-size: 11.8px 11.8px;
    background-position: -0.5px -0.5px;
  }
</style>
</head>
<body>
<div class="canvas">
  <section class="sheet">
    <svg class="header-wave" viewBox="0 0 433 62" role="img" aria-label="Soft blue wave band across the top right of the sheet">
      <defs>
        <linearGradient id="waveFade" x1="0" y1="0" x2="1" y2="0">
          <stop offset="0" stop-color="#85abd2" stop-opacity="0"/>
          <stop offset=".45" stop-color="#85abd2" stop-opacity=".35"/>
          <stop offset="1" stop-color="#3f9ad6" stop-opacity=".6"/>
        </linearGradient>
        <linearGradient id="waveLight" x1="0" y1="0" x2="1" y2="0">
          <stop offset="0" stop-color="#bfe3f5" stop-opacity="0"/>
          <stop offset="1" stop-color="#bfe3f5" stop-opacity=".9"/>
        </linearGradient>
      </defs>
      <path d="M150 0 H433 V40 C380 30 330 14 280 18 C240 21 210 10 150 0 Z" fill="url(#waveFade)"/>
      <path d="M190 0 H433 V22 C390 12 340 2 300 8 C260 13 230 4 190 0 Z" fill="url(#waveLight)"/>
    </svg>

    <div class="brand">
      <span class="brand-name">Morvaleth Company</span>
      <span class="brand-tagline">Structural | Precise | Trusted</span>
    </div>

    <address class="contact">
      215 Larkspur Avenue, Suite 204, Coral Harbor, FL 33190<br>
      555.014.2736 | www.morvalethcompany.com
    </address>

    <div class="fields">
      <div class="field-row">
        <div class="field field--wide"><span class="field-label">Project</span><span class="field-line"></span></div>
        <div class="field field--narrow"><span class="field-label">&nbsp;Job No</span><span class="field-line"></span></div>
      </div>
      <div class="field-row">
        <div class="field field--wide"><span class="field-label">Task</span><span class="field-line"></span></div>
        <div class="field field--narrow"><span class="field-label">&nbsp;Author</span><span class="field-line"></span></div>
      </div>
      <div class="field-row">
        <div class="field field--page"><span class="field-label">Page</span><span class="field-line"></span></div>
        <div class="field field--of"><span class="field-label">of</span><span class="field-line"></span></div>
        <div class="field field--narrow"><span class="field-label">&nbsp;Date</span><span class="field-line"></span></div>
      </div>
    </div>

    <div class="grid-area" aria-label="Graph grid writing area"></div>
  </section>
</div>
</body>
</html>
```